Property maintenance company needs an eye catching postcard design

We are a property maintenance company that wants to send out a postcard targeting residential homeowners only. We want the postcard to create the impression of a friendly and inviting company that makes maintenance easy for homeowners. I have attached all the instructions in a pdf file as well as any other needed pictures or info. Please read the outline I provided. I also attached pictures/screenshots of our new (in progress) website if you wish to get a feel for our company.

Thanks!

Target Market(s)

residential homeowners, homeowners

Industry/Entity Type

Property Maintenance

```html
<!DOCTYPE html>
<html lang="en">
<head>
<meta charset="utf-8">
<title>HomeLink Postcard</title>
<link href="https://fonts.googleapis.com/css2?family=Didact+Gothic&family=Montserrat:wght@700&family=Arimo:wght@400;700&display=swap" rel="stylesheet">
<style>
  :root{
    --page:#e2e2e2;
    --navy:#2a3a8e;
    --navy-light:#5270bd;
    --green:#6fbe44;
    --ink:#333333;
    --white:#ffffff;
    --sky:#6f9ad8;
    --lawn:#7bb24a;
  }
  *{margin:0;padding:0;box-sizing:border-box;}
  html,body{width:1200px;height:2169px;overflow:hidden;background:var(--page);}
  body{position:relative;font-family:"Didact Gothic",sans-serif;}
  .card{position:absolute;left:50px;width:990px;transform-origin:0 0;transform:scale(1.1111);
        background:var(--white);overflow:hidden;box-shadow:0 10px 22px rgba(0,0,0,.28);}
  .card--front{top:290px;height:652px;}
  .card--back{top:1145px;height:657px;}
  .card svg.shapes{position:absolute;left:0;top:0;}
  .abs{position:absolute;white-space:nowrap;}

  /* front */
  .headline-tag{left:243px;top:48px;width:542px;height:58px;background:var(--green);
        color:var(--white);font-size:49px;line-height:60px;text-align:center;letter-spacing:.5px;}
  .headline-main{left:0;width:1028px;top:110px;text-align:center;font-family:"Montserrat",sans-serif;
        font-weight:700;font-size:47px;color:var(--white);text-shadow:0 2px 6px rgba(0,0,0,.35);}
  .pitch{left:71px;font-size:31px;color:var(--ink);line-height:34px;}
  .pitch--strong{font-family:"Montserrat",sans-serif;font-weight:700;color:var(--navy);font-size:28px;}
  .front-phone{left:71px;top:570px;font-family:"Montserrat",sans-serif;font-weight:700;font-size:28px;color:var(--green);}
  .brand{display:flex;align-items:center;gap:14px;}
  .brand__mark{width:30px;height:30px;background:var(--green);}
  .brand__name{font-family:"Didact Gothic",sans-serif;}
  .brand--front{left:560px;top:503px;}
  .brand--front .brand__name{font-size:50px;color:var(--navy);}
  .front-url{left:495px;top:610px;font-size:22px;color:var(--white);letter-spacing:1.5px;}

  /* back */
  .brand--back{left:62px;top:70px;}
  .brand--back .brand__mark{width:24px;height:24px;}
  .brand--back .brand__name{font-size:36px;color:var(--white);}
  .tag{left:52px;background:var(--green);color:var(--white);padding:0 8px;}
  .tag--what{top:195px;height:30px;font-size:24px;line-height:31px;}
  .tag--services{top:325px;height:34px;font-size:25px;line-height:35px;}
  .tag--call{top:508px;height:38px;font-size:31px;line-height:39px;}
  .offer{left:52px;top:230px;color:var(--white);font-size:18px;line-height:22px;}
  .service-label{top:437px;color:var(--white);font-size:18px;transform:translateX(-50%);}
  .back-phone{left:52px;top:558px;font-family:"Montserrat",sans-serif;font-weight:700;font-size:27px;color:var(--white);}
  .back-url{left:52px;top:590px;font-size:21px;color:var(--white);letter-spacing:1.2px;}
  .indicia{left:821px;top:28px;width:135px;height:100px;border:1.5px solid #333;font-family:"Arimo",sans-serif;
        font-size:14px;line-height:18px;text-align:center;padding-top:4px;color:#222;}
  .indicia b{font-size:16px;}
  .mail-block{left:717px;top:202px;width:236px;height:86px;border:1.5px solid #333;font-family:"Arimo",sans-serif;
        font-size:12px;color:#222;padding:6px 0 0 14px;line-height:16px;}
  .mail-block .route{margin-bottom:16px;}
</style>
</head>
<body>

<section class="card card--front" aria-label="Postcard front">
  <svg class="shapes" width="990" height="652" viewBox="0 0 990 652">
    <defs>
      <linearGradient id="scene" x1="0" y1="0" x2="0" y2="1">
        <stop offset="0" stop-color="#4f86d6"/>
        <stop offset=".45" stop-color="#a9c4e4"/>
        <stop offset=".7" stop-color="#5b7398"/>
        <stop offset="1" stop-color="#6ea845"/>
      </linearGradient>
      <linearGradient id="band" x1="0" y1="0" x2="1" y2="0">
        <stop offset="0" stop-color="#2a3a8e"/>
        <stop offset="1" stop-color="#5270bd"/>
      </linearGradient>
    </defs>
    <rect width="990" height="470" fill="url(#scene)" role="img" aria-label="Photo of a sunny residential street with painted houses, lawns and trees"/>
    <path d="M0,444 Q500,362 990,424 L990,442 Q500,386 0,454 Z" fill="var(--green)"/>
    <path d="M0,454 Q500,386 990,442 L990,652 L0,652 Z" fill="var(--white)"/>
    <path d="M0,652 L0,646 Q420,598 990,588 L990,652 Z" fill="url(#band)"/>
  </svg>
  <div class="abs headline-tag">HOMELINK MAKES</div>
  <div class="abs headline-main">HOME MAINTENANCE EASY</div>
  <div class="abs pitch" style="top:458px">ONE POINT OF CONTACT</div>
  <div class="abs pitch" style="top:492px">FOR ALL YOUR PROPERTY</div>
  <div class="abs pitch pitch--strong" style="top:527px">MAINTENANCE NEEDS</div>
  <div class="abs front-phone">PHONE: 555-014-2277</div>
  <div class="abs brand brand--front"><span class="brand__mark"></span><span class="brand__name">HOMELINK</span></div>
  <div class="abs front-url">www.homelinkmaint.com</div>
</section>

<section class="card card--back" aria-label="Postcard back">
  <svg class="shapes" width="990" height="657" viewBox="0 0 990 657">
    <defs>
      <linearGradient id="panel" x1="0" y1="0" x2="1" y2="1">
        <stop offset="0" stop-color="#2a3a8e"/>
        <stop offset="1" stop-color="#5270bd"/>
      </linearGradient>
      <linearGradient id="house" x1="0" y1="0" x2="0" y2="1">
        <stop offset="0" stop-color="#8aa0b8"/>
        <stop offset=".5" stop-color="#3d4f6a"/>
        <stop offset="1" stop-color="#6a8d4a"/>
      </linearGradient>
      <linearGradient id="interior" x1="0" y1="0" x2="1" y2="0">
        <stop offset="0" stop-color="#6b5a3a"/>
        <stop offset=".6" stop-color="#e6e0d4"/>
        <stop offset="1" stop-color="#f4f2ee"/>
      </linearGradient>
    </defs>
    <path d="M0,0 L560,0 Q680,330 552,657 L0,657 Z" fill="var(--green)"/>
    <path d="M0,0 L548,0 Q662,330 540,657 L0,657 Z" fill="url(#panel)"/>
    <path d="M310,0 L555,0 Q575,80 586,160 L350,160 Q330,80 310,0 Z" fill="url(#house)" role="img" aria-label="Photo of a two-storey family home exterior"/>
    <path d="M382,172 L590,172 Q600,250 600,330 L386,330 Q395,250 382,172 Z" fill="url(#interior)" role="img" aria-label="Photo of a bright renovated living room interior"/>
    <g fill="none" stroke="var(--green)" stroke-width="2.4" stroke-linecap="round" stroke-linejoin="round">
      <circle cx="93" cy="410" r="15"/>
      <path d="M97,398 L86,412 L95,412 L89,423"/>
      <path d="M186,396 L214,424 M214,396 L186,424 M182,400 l6,-6 M218,420 l-6,6"/>
      <path d="M273,422 L279,398 L313,398 L319,422 Z M282,398 L279,422 M293,398 L292,422 M304,398 L305,422 M276,410 L316,410"/>
      <path d="M386,398 L410,398 M398,392 L398,404 M398,404 L398,412 L410,412 Q416,412 416,420 L416,424 M386,412 L398,412"/>
      <path d="M498,424 L522,398 M516,394 l10,10 M524,424 L500,398 M494,402 l8,-8"/>
    </g>
    <rect x="408" y="583" width="127" height="47" rx="5" fill="var(--white)"/>
  </svg>
  <div class="abs brand brand--back"><span class="brand__mark"></span><span class="brand__name">HOMELINK</span></div>
  <div class="abs tag tag--what">What We do</div>
  <div class="abs offer">Maintenance Packages<br>General Maintenance/Handyman<br>Repairs Home Renovations</div>
  <div class="abs tag tag--services">Services</div>
  <div class="abs service-label" style="left:93px">Electrical</div>
  <div class="abs service-label" style="left:201px">Millwork</div>
  <div class="abs service-label" style="left:296px">Flooring</div>
  <div class="abs service-label" style="left:398px">Plumbing</div>
  <div class="abs service-label" style="left:511px">Carpentry</div>
  <div class="abs tag tag--call">Call Us Now</div>
  <div class="abs back-phone">555-014-2277</div>
  <div class="abs back-url">www.homelinkmaint.com</div>
  <div class="abs indicia">PRSRT STD<br>ECRWSS<br>U.S.POSTAGE<br><b>PAID</b><br>EDDM Retail</div>
  <div class="abs mail-block"><div class="route">****************ECRWSSEDDM****</div>Postal Customer<br>City, State, 5-Digit ZIP Code</div>
</section>

</body>
</html>
```